Bulk Food Container sticker

Our company sells bulk snacks to office locations. We re-package all sorts of foods into re-usable "Vessaline" type containers for consistency. We need to create a designed sticker which has room to laser-print the name of the food. The "blank" sticker needs to be designed with our logo, etc... I have attached 2 files. The first is an example from another company doing a similar work, and the second is the template from the company that will be printing the stickers for me. See our website for examples of our current corporate identity. www.brindlemoorbeans.com
Target Market(s)
Offices, tech companies
Industry/Entity Type
Printing
Look and feel

```html
<!DOCTYPE html>
<html lang="en">
<head>
<meta charset="utf-8">
<title>Brindlemoor Coffee Service – Container Sticker</title>
<link rel="stylesheet" href="https://fonts.googleapis.com/css2?family=Arimo:wght@400;700&display=swap">
<style>
  :root {
    --brown-deep: #2e1810;
    --brown-mid: #5a3424;
    --brown-name: #6b3d1e;
    --panel-white: #ffffff;
    --silver: #c9c9c9;
    --ink: #111111;
    --texture-light: #fbf1e0;
    --texture-warm: #f1d9ae;
  }
  html, body {
    margin: 0;
    padding: 0;
    width: 1178px;
    height: 1200px;
    overflow: hidden;
    background: #ffffff;
  }
  .sticker {
    display: block;
    width: 1178px;
    height: 1200px;
  }
  .brand-name {
    font-family: "Arimo", Arial, sans-serif;
    font-weight: 400;
    font-size: 24px;
    fill: var(--brown-name);
  }
  .brand-dot {
    fill: var(--brown-name);
  }
</style>
</head>
<body>
<svg class="sticker" viewBox="0 0 420 428" preserveAspectRatio="none" xmlns="http://www.w3.org/2000/svg">
  <defs>
    <linearGradient id="bg-brown" x1="0" y1="0" x2="0" y2="1">
      <stop offset="0" stop-color="var(--brown-deep)"/>
      <stop offset="0.2" stop-color="var(--brown-mid)"/>
      <stop offset="0.8" stop-color="var(--brown-mid)"/>
      <stop offset="1" stop-color="var(--brown-deep)"/>
    </linearGradient>
    <linearGradient id="texture-fade" x1="0" y1="0" x2="1" y2="0">
      <stop offset="0" stop-color="var(--texture-warm)" stop-opacity="0.9"/>
      <stop offset="0.55" stop-color="var(--texture-light)" stop-opacity="0.8"/>
      <stop offset="1" stop-color="var(--panel-white)" stop-opacity="0"/>
    </linearGradient>
    <clipPath id="panel-clip">
      <path d="M0 98 C 110 70, 230 62, 330 60 C 370 59, 400 62, 420 70 L420 340 C 390 350, 340 366, 280 364 C 200 360, 90 330, 0 330 Z"/>
    </clipPath>
  </defs>

  <rect class="sticker-field" x="0" y="0" width="420" height="428" fill="url(#bg-brown)"/>

  <path class="swoosh-top" d="M0 88 C 110 58, 230 52, 330 50 C 370 49, 400 54, 420 62 L420 70 C 400 62, 370 59, 330 60 C 230 62, 110 70, 0 98 Z" fill="var(--silver)"/>

  <path class="label-panel" d="M0 98 C 110 70, 230 62, 330 60 C 370 59, 400 62, 420 70 L420 340 C 390 350, 340 366, 280 364 C 200 360, 90 330, 0 330 Z" fill="var(--panel-white)"/>

  <rect class="texture-area" role="img" aria-label="Soft beige distressed paint texture" x="0" y="55" width="110" height="320" fill="url(#texture-fade)" clip-path="url(#panel-clip)"/>

  <path class="panel-edge-top" d="M0 98 C 110 70, 230 62, 330 60 C 370 59, 400 62, 420 70" fill="none" stroke="var(--ink)" stroke-width="2.2"/>
  <path class="panel-edge-bottom" d="M0 330 C 90 330, 200 360, 280 364 C 340 366, 390 350, 420 340" fill="none" stroke="var(--ink)" stroke-width="2.5"/>
  <path class="swoosh-bottom" d="M0 338 C 90 340, 200 370, 280 373 C 340 375, 390 360, 420 350" fill="none" stroke="var(--silver)" stroke-width="2.5"/>

  <rect class="cut-line" x="18" y="20" width="384" height="390" rx="14" ry="14" fill="none" stroke="var(--ink)" stroke-width="1.5"/>

  <circle class="brand-dot" cx="62" cy="150" r="7"/>
  <text class="brand-name" x="78" y="158">Brindlemoor Coffee Service</text>
</svg>
</body>
</html>
```